High Converting Mobile Site Design

We need a mobile site design for a new company called "Wheels of Wonder" - wheelsofwonder.com.au. The website will specialise in selling electric ride on toy Wheels of wonder.

Wheels of wonder is a new Australian company that offers the cheapest prices on kids ride on toys. With a huge selection of ride on toy cars and bikes, Wheels of Wonder the best place to buy the cheapest ride on car.

Target Market(s)

Parents in Australia and New Zealand

Industry/Entity Type

E-Commerce

Number of Pages Required

4 page

Font styles to use
Sans Serif

Colors

Designer to choose colors to be used in the design.

Requirements
Must have
• The design will need to have:
• Homepage:
• - H1 / Hero Image / Lead in text / All products / SEO Text / Footer
• Category Pages: Which has the different product categories (e.g. Zelms / Quads / Varno’s etc.)
• - This will need to include H1 / Lead in Paragraph / Category of Projects / Lead out SEO text (4 paragraphs)
• Product Page: Details of the specific product that is being advertised
• - This will need to include: H1 / Sub Head / Image Gallery / Product Specs / Quick Specs (Image Based) / Price / Shipping Calculator / Quantity Selection / Add to Cart Button / Product Description / Product Video / Full Product Specs / FAQs / SEO Text
• Content Page: H1 / Product List / Content (600-800 words)
• Checkout Page:
• - This will need to include: - Add Ons / Billing & Shipping Details (First Name, Last Name, Email, Phone, Delivery Address, State, Postcode - Order Details - Payment Options (Credit Card, SendTuk, Bank Transfer)
• Other Requirements:
• All pages need to contain a footer and a header. The footer will need to leave space so that we can have a number of links (copyright, about us, top products, content articles etc.).
Nice to have
• From a design perspective, we want a very clear, and usable design. It should be intuitive, obvious and of course mobile friendly. Please take clean design elements from the largest US e-Commerce mobile sites...
• - https://www.brindlemart.com/
• - https://www.quillop.com/
• - https://www.topshelfo.com/?intl=nosplash
• - https://www.yardhaven.com/
• - https://www.mellowvane.com/S-7iiWIpYTD28/
• Here is an example of an Australian ride on toy company - https://www.tynyrovr.com.au that we will have similar features too.
• The website will eventually be developed into a desktop site, so any design will need to follow the bootstrap grid.

```html
<!DOCTYPE html>
<html lang="en">
<head>
<meta charset="utf-8">
<title>Wheels of wonder – Mobile Home</title>
<link href="https://fonts.googleapis.com/css2?family=Montserrat:wght@400;500&family=Open+Sans:wght@400;600;700;800&display=swap" rel="stylesheet">
<style>
:root{
  --brand-red:#ec5a5c;
  --welcome-purple:#7b5ec6;
  --product-green:#1bab80;
  --product-green-dark:#15936d;
  --seo-blue:#8fb6d9;
  --panel-grey:#eeeeee;
  --text-body:#3a3a3a;
  --footer-bg:#2b2b2b;
  --footer-text:#cfcfcf;
  --footer-muted:#a8a8a8;
  --button-dark:#333333;
  --white:#ffffff;
}
*{box-sizing:border-box;margin:0;padding:0}
html,body{width:1200px;height:5042px;overflow:hidden}
body{font-family:"Open Sans",Arial,sans-serif;color:var(--text-body);background:var(--white)}

.site-header{height:188px;background:var(--brand-red);display:flex;align-items:center;justify-content:space-between;padding:0 52px 0 54px}
.brand{font-family:"Montserrat",Arial,sans-serif;font-weight:500;font-size:70px;color:var(--white)}
.header-actions{display:flex;gap:48px;align-items:center}

.hero{position:relative;height:935px;background:linear-gradient(180deg,#b9ab80 0%,#8f8a72 55%,#6f6d60 100%)}
.hero-copy{position:absolute;right:30px;top:262px;text-align:right;color:var(--white);text-shadow:0 2px 6px rgba(0,0,0,.35)}
.hero-title{font-weight:800;font-size:62px;line-height:72px;letter-spacing:1px;text-transform:uppercase}
.hero-lead{font-size:37px;line-height:50px;margin-top:8px}
.slider-dots{position:absolute;left:0;right:0;top:864px;display:flex;justify-content:center;gap:38px}
.dot{width:32px;height:32px;border-radius:50%;background:var(--white)}
.dot.is-active{background:var(--brand-red);border:5px solid var(--white)}

.welcome{height:510px;text-align:center;padding:108px 54px 0}
.section-title{font-weight:800;text-transform:uppercase;font-size:64px;line-height:80px}
.welcome .section-title{color:var(--welcome-purple)}
.body-copy{font-size:27px;line-height:43px;margin-top:8px}

.products{height:1969px;background:var(--panel-grey);padding-top:128px;text-align:center}
.products .section-title{color:var(--product-green)}
.product-grid{display:grid;grid-template-columns:508px 508px;column-gap:70px;row-gap:73px;justify-content:center;margin-top:38px}
.product-card{text-align:center}
.product-image{height:375px}
.product-info{height:188px;background:var(--product-green);color:var(--white);padding-top:40px}
.product-name{font-size:35px;line-height:46px}
.product-price{font-size:44px;font-weight:700;line-height:58px}
.add-to-cart{height:95px;background:var(--product-green-dark);color:var(--white);display:flex;align-items:center;justify-content:center;gap:14px;font-size:28px;font-weight:600;text-transform:uppercase}
.view-all{display:inline-flex;align-items:center;justify-content:center;width:206px;height:91px;margin-top:84px;background:var(--button-dark);color:var(--white);font-size:37px}

.seo{height:1143px;text-align:center;padding:160px 54px 0}
.seo .section-title{color:var(--seo-blue);font-size:63px}
.seo .body-copy{margin-top:14px}
.seo .body-copy + .body-copy{margin-top:22px}

.site-footer{height:297px;background:var(--footer-bg);color:var(--footer-text);text-align:center;padding-top:52px;font-size:26px}
.footer-links{display:flex;justify-content:center;gap:14px}
.copyright{margin-top:22px}
.footer-bottom{display:flex;justify-content:center;align-items:center;gap:120px;margin-top:58px;font-size:26px;color:var(--footer-muted)}
.social-list,.payment-list{display:flex;gap:34px}
</style>
</head>
<body>
<header class="site-header">
  <div class="brand">Wheels of wonder</div>
  <div class="header-actions">
    <svg width="62" height="52" viewBox="0 0 62 52" aria-label="Menu"><rect y="0" width="62" height="9" fill="#fff"/><rect y="21" width="62" height="9" fill="#fff"/><rect y="42" width="62" height="9" fill="#fff"/></svg>
    <svg width="70" height="60" viewBox="0 0 70 60" aria-label="Cart"><path d="M2 4h12l8 32h38l8-26H18" fill="none" stroke="#fff" stroke-width="7" stroke-linejoin="round"/><path d="M20 10h46l-8 24H24z" fill="#fff"/><circle cx="27" cy="51" r="6" fill="#fff"/><circle cx="55" cy="51" r="6" fill="#fff"/></svg>
  </div>
</header>

<section class="hero" role="img" aria-label="Photo of a young boy driving a red pedal car on a sunlit country road">
  <div class="hero-copy">
    <h1 class="hero-title">Aenean faucibus<br>lacus mollis</h1>
    <p class="hero-lead">Donec vestibulum odio sem, ac<br>laoreet massa ullamcorper</p>
  </div>
  <div class="slider-dots"><span class="dot is-active"></span><span class="dot"></span><span class="dot"></span><span class="dot"></span></div>
</section>

<section class="welcome">
  <h2 class="section-title">Welcome</h2>
  <p class="body-copy">Donec molestie nisi et tellus hendrerit vehicula. Nunc eu ligula sed quam pulvinar maximus in vitae eros. Proin porta fermentum ipsum, vel porttitor turpis venenatis luctus. Vivamus volutpat eu sapien quis tempus. Aenean feugiat viverra lorem ac sagittis. Donec sit amet lectus nec mi tempor laoreet ac nec</p>
</section>

<section class="products">
  <h2 class="section-title">Products</h2>
  <div class="product-grid">
    <article class="product-card">
      <div class="product-image" role="img" aria-label="Photo of a child in a silver ride-on car on a grassy lane" style="background:linear-gradient(180deg,#93a868 0%,#a5a595 100%)"></div>
      <div class="product-info"><p class="product-name">Nullam accumsan purus</p><p class="product-price">$420</p></div>
      <div class="add-to-cart"><svg width="30" height="26" viewBox="0 0 70 60"><path d="M2 4h12l8 32h38l8-26H18z" fill="#fff"/><circle cx="27" cy="51" r="7" fill="#fff"/><circle cx="55" cy="51" r="7" fill="#fff"/></svg>Add to cart</div>
    </article>
    <article class="product-card">
      <div class="product-image" role="img" aria-label="Photo of a child in a white electric ride-on sports car by the sea" style="background:linear-gradient(180deg,#8fb0d0 0%,#c2b8a6 100%)"></div>
      <div class="product-info"><p class="product-name">Mauris suscipit felis</p><p class="product-price">$450</p></div>
      <div class="add-to-cart"><svg width="30" height="26" viewBox="0 0 70 60"><path d="M2 4h12l8 32h38l8-26H18z" fill="#fff"/><circle cx="27" cy="51" r="7" fill="#fff"/><circle cx="55" cy="51" r="7" fill="#fff"/></svg>Add to cart</div>
    </article>
    <article class="product-card">
      <div class="product-image" role="img" aria-label="Photo of a child in a vintage silver ride-on car under green trees" style="background:linear-gradient(180deg,#7e9c58 0%,#a4a898 100%)"></div>
      <div class="product-info"><p class="product-name">Praesent elementum</p><p class="product-price">$437</p></div>
      <div class="add-to-cart"><svg width="30" height="26" viewBox="0 0 70 60"><path d="M2 4h12l8 32h38l8-26H18z" fill="#fff"/><circle cx="27" cy="51" r="7" fill="#fff"/><circle cx="55" cy="51" r="7" fill="#fff"/></svg>Add to cart</div>
    </article>
    <article class="product-card">
      <div class="product-image" role="img" aria-label="Photo of a child in a helmet riding a blue ride-on car on grass" style="background:linear-gradient(180deg,#c6d9e8 0%,#6f9a55 100%)"></div>
      <div class="product-info"><p class="product-name">Vivamus gravida</p><p class="product-price">$462</p></div>
      <div class="add-to-cart"><svg width="30" height="26" viewBox="0 0 70 60"><path d="M2 4h12l8 32h38l8-26H18z" fill="#fff"/><circle cx="27" cy="51" r="7" fill="#fff"/><circle cx="55" cy="51" r="7" fill="#fff"/></svg>Add to cart</div>
    </article>
  </div>
  <a class="view-all">View All</a>
</section>

<section class="seo">
  <h2 class="section-title">Donec vestibulum odio</h2>
  <p class="body-copy">Donec molestie nisi et tellus hendrerit vehicula. Nunc eu ligula sed quam pulvinar maximus in vitae eros. Proin porta fermentum ipsum, vel porttitor turpis venenatis luctus. Vivamus volutpat eu sapien quis tempus. Aenean feugiat viverra lorem ac sagittis. Donec sit amet lectus nec mi tempor laoreet ac nec nunc.</p>
  <p class="body-copy">Nullam accumsan purus vel tempus viverra. Mauris suscipit felis id nunc elementum varius. Praesent elementum nulla sit amet justo pellentesque scelerisque. Nam et tortor in ante iaculis porttitor in luctus mi.</p>
  <p class="body-copy">Vivamus gravida sem a pretium euismod. Nam lobortis, purus et fringilla tempus, risus eros dignissim diam, eget finibus sem risus sit amet eros. Vestibulum facilisis dolor at purus tincidunt porta. Nam fringilla nulla vel nisl condimentum, dapibus condimentum enim porta.</p>
  <p class="body-copy">Phasellus blandit quam a ipsum gravida dapibus. Cras sed augue tortor. Suspendisse elit ligula, iaculis dignissim justo eu, vestibulum venenatis elit. Sed egestas, nisl id cursus ultricies, turpis orci rhoncus odio, id tristique odio ex in lacus. Nam suscipit sapien eget blandit sollicitudin.</p>
</section>

<footer class="site-footer">
  <nav class="footer-links"><span>Home</span>|<span>Products</span>|<span>Offers</span>|<span>Support</span>|<span>My Account</span>|<span>My Cart</span>|<span>Checkout</span></nav>
  <p class="copyright">Copyright © 2018 Wheels of wonder. All rights reserved.</p>
  <div class="footer-bottom">
    <div class="social-list"><span>Friendwall</span><span>Chirpa</span><span>Plusly</span><span>Snapgrid</span></div>
    <div class="payment-list"><span>SendTuk</span><span>Circlo</span><span>Vantra</span><span>Dyscova</span></div>
  </div>
</footer>
</body>
</html>
```